Business card for home decor store and design

I need a business card for my home decor boutique that’s professional looking boho/rustic. We sell vintage furniture, vintage finds, lamps, throws, rugs. We also carry a Diy paint line for refinishing furniture. We offer workshop on painting furniture, private or group setting. We in the heart of Old Town Red Bluff. We love to design, build and restore. Family owned small business. Our style is rustic boho farmhouse. We search for one of a kind found and repurposed items. We love vintage home decor, vintage windows.

Target Market(s)

Home decor

Industry/Entity Type

Home Accessories

Contact Information for Business Card

Have a rustic look/boho

Font styles to use
Serif
Script

Requirements
Must have
• Logo

```html
<!DOCTYPE html>
<html lang="en">
<head>
<meta charset="utf-8">
<title>Juniper &amp; Loam Co. — Business Card</title>
<link href="https://fonts.googleapis.com/css2?family=Montserrat:wght@400;500;600;700;800&display=swap" rel="stylesheet">
<style>
  :root {
    --backdrop: #232323;
    --wood-light: #f0d3b1;
    --wood-mid: #e2b98f;
    --wood-deep: #d3a57a;
    --ink: #111111;
    --band: #0a0a0a;
    --band-text: #ffffff;
  }
  * { box-sizing: border-box; margin: 0; padding: 0; }
  html, body {
    width: 1200px; height: 781px; overflow: hidden;
    background: var(--backdrop);
    font-family: "Montserrat", Arial, sans-serif;
    color: var(--ink);
  }
  .stage {
    position: relative; width: 1200px; height: 781px;
    display: flex; align-items: center; justify-content: center; gap: 40px;
  }
  .card {
    position: relative; width: 540px; height: 310px;
    border-radius: 26px; overflow: hidden;
    box-shadow: 0 10px 28px rgba(0,0,0,.55);
  }
  .card__wood {
    position: absolute; inset: 0;
    background:
      linear-gradient(180deg, rgba(255,255,255,.08) 0 20%, transparent 20% 40%, rgba(0,0,0,.04) 40% 60%, transparent 60% 80%, rgba(255,255,255,.06) 80%),
      linear-gradient(100deg, var(--wood-light) 0%, var(--wood-mid) 45%, var(--wood-light) 70%, var(--wood-deep) 100%);
  }
  .card__band {
    position: absolute; left: 0; right: 0; bottom: 0; height: 58px;
    background: var(--band); color: var(--band-text);
    display: flex; align-items: center; justify-content: center; gap: 22px;
    font-size: 17px; font-weight: 500; letter-spacing: .5px;
  }
  .card__body { position: absolute; left: 0; right: 0; top: 0; bottom: 58px; }

  .brand {
    display: flex; align-items: center; gap: 10px;
    font-weight: 700; color: var(--ink); white-space: nowrap;
  }
  .brand__dot { border-radius: 50%; border: 3px solid var(--ink); flex: none; }

  .divider { position: relative; height: 2px; background: var(--ink); width: 100%; }
  .divider::before, .divider::after {
    content: ""; position: absolute; top: -3px; width: 8px; height: 8px;
    border-radius: 50%; background: var(--ink);
  }
  .divider::before { left: -2px; }
  .divider::after { right: -2px; }

  /* Back side */
  .card--services .card__body {
    display: flex; flex-direction: column; align-items: center; justify-content: center;
    text-align: center; gap: 10px; padding: 0 40px;
  }
  .card--services .brand { font-size: 20px; }
  .card--services .brand__dot { width: 26px; height: 26px; }
  .service { font-size: 15px; line-height: 1.3; }
  .service strong { font-weight: 800; }

  /* Front side */
  .card--contact .brand {
    position: absolute; left: 24px; top: 118px; font-size: 19px;
  }
  .card--contact .brand__dot { width: 32px; height: 32px; }
  .person { position: absolute; left: 272px; right: 22px; top: 38px; text-align: right; }
  .person__name { font-size: 26px; font-weight: 800; letter-spacing: .2px; white-space: nowrap; }
  .person__role { font-size: 15px; font-weight: 400; margin-top: 2px; }
  .person .divider { margin-top: 12px; }
  .contact-list { list-style: none; position: absolute; left: 272px; right: 22px; top: 132px; }
  .contact-list li {
    display: flex; align-items: center; gap: 8px;
    font-size: 13px; font-weight: 600; margin-bottom: 10px; white-space: nowrap;
  }
  .contact-list svg { flex: none; }
</style>
</head>
<body>
<main class="stage">

  <section class="card card--services">
    <div class="card__wood" role="img" aria-label="Light maple wood plank texture"></div>
    <div class="card__body">
      <div class="brand"><span class="brand__dot"></span><span>Juniper &amp; Loam Co.</span></div>
      <p class="service"><strong>We sell</strong> vintage furniture,<br>vintage finds, lamps, throws, rugs.</p>
      <div class="divider"></div>
      <p class="service"><strong>We offer</strong> workshop on painting furniture,<br>private or group setting.</p>
    </div>
    <div class="card__band">
      <span>Home decor</span><span>|</span><span>Furniture</span><span>|</span><span>Antiques shop</span>
    </div>
  </section>

  <section class="card card--contact">
    <div class="card__wood" role="img" aria-label="Light maple wood plank texture"></div>
    <div class="card__body">
      <div class="brand"><span class="brand__dot"></span><span>Juniper &amp; Loam Co.</span></div>
      <div class="person">
        <h1 class="person__name">Marla Quennell</h1>
        <p class="person__role">Owner and Founder</p>
        <div class="divider"></div>
      </div>
      <ul class="contact-list">
        <li>
          <svg width="20" height="20" viewBox="0 0 20 20" aria-hidden="true">
            <circle cx="10" cy="10" r="10" fill="#111"/>
            <path d="M6.5 5c.6 0 1.6 2 1.6 2.5 0 .6-1 1-.9 1.5.3 1.3 2.2 3.3 3.6 3.6.5.1 1-.9 1.5-.9s2.4 1 2.4 1.6c0 .9-1 1.8-2 1.8-3 0-7.3-4.3-7.3-7.3C5.4 6 5.9 5 6.5 5z" fill="#fff"/>
          </svg>
          <span>+1 555-014-2290</span>
        </li>
        <li>
          <svg width="20" height="20" viewBox="0 0 20 20" aria-hidden="true">
            <circle cx="10" cy="10" r="10" fill="#111"/>
            <rect x="5" y="6.5" width="10" height="7" fill="none" stroke="#fff" stroke-width="1.3"/>
            <path d="M5 6.5l5 4 5-4" fill="none" stroke="#fff" stroke-width="1.3"/>
          </svg>
          <span>juniperandloam@example.com</span>
        </li>
      </ul>
    </div>
    <div class="card__band">
      <span>Home decor</span><span>|</span><span>Furniture</span><span>|</span><span>Antiques shop</span>
    </div>
  </section>

</main>
</body>
</html>
```